Morvela Aesthetic Doctor

I require an elegant, luxurious looking business card for my aesthetic business. I am a doctor and that will set me aside from competitors. I am planning to provide home and spa based treatments to clients with high expectations. I have attached my logo.

```html
<!DOCTYPE html>
<html lang="en">
<head>
<meta charset="utf-8">
<title>Morvela Aesthetic Doctor – Business Card</title>
<link rel="stylesheet" href="https://fonts.googleapis.com/css2?family=Montserrat:wght@700&family=Open+Sans:wght@400;600&display=swap">
<style>
  :root {
    --canvas: #8a8a8a;
    --card-light: #ffffff;
    --card-dark: #2f2e30;
    --brand-blue: #1aa3e0;
    --soft-blue: #a9d4ee;
    --pale-blue: #dcedf8;
    --ink: #2d2d2d;
    --muted: #6b6b6b;
    --rule: #3a3a3a;
    --ring: #c9c9c9;
    --logo-grey: #d9d9d9;
  }
  * { box-sizing: border-box; margin: 0; padding: 0; }
  html, body { width: 1200px; height: 856px; overflow: hidden; }
  body {
    background: var(--canvas);
    font-family: "Open Sans", Arial, sans-serif;
    display: flex;
    flex-direction: column;
    align-items: center;
    justify-content: center;
    gap: 40px;
  }
  .card {
    position: relative;
    width: 640px;
    height: 366px;
    border-radius: 28px;
    overflow: hidden;
    box-shadow: 0 6px 18px rgba(0,0,0,0.25);
  }

  /* Back side */
  .card--back { background: var(--card-dark); }
  .brand-lockup {
    position: absolute;
    left: 0; right: 0; top: 140px;
    display: flex;
    align-items: center;
    justify-content: center;
    gap: 18px;
  }
  .brand-mark {
    width: 46px; height: 46px;
    border-radius: 50%;
    border: 2px solid var(--logo-grey);
  }
  .brand-name {
    font-family: "Open Sans", Arial, sans-serif;
    font-weight: 400;
    font-size: 34px;
    letter-spacing: 3px;
    color: var(--logo-grey);
  }
  .back-tagline {
    position: absolute;
    right: 54px; bottom: 62px;
    font-size: 13px;
    font-weight: 600;
    color: var(--brand-blue);
  }

  /* Front side */
  .card--front { background: var(--card-light); }
  .hero-art {
    position: absolute;
    left: -40px; top: 92px;
    width: 290px; height: 200px;
    border-radius: 0 50% 50% 0;
    background: linear-gradient(160deg, var(--pale-blue) 0%, var(--soft-blue) 55%, var(--pale-blue) 100%);
    border-right: 3px solid var(--ring);
  }
  .identity {
    position: absolute;
    right: 44px; top: 26px;
    text-align: right;
  }
  .identity__name {
    font-family: "Montserrat", Arial, sans-serif;
    font-weight: 700;
    font-size: 27px;
    letter-spacing: 1px;
    color: var(--brand-blue);
  }
  .identity__credentials {
    font-size: 11px;
    color: var(--muted);
    line-height: 1.35;
  }
  .contact {
    position: absolute;
    left: 400px; top: 120px;
    list-style: none;
    font-size: 14px;
    color: var(--ink);
  }
  .contact li { display: flex; align-items: center; gap: 10px; line-height: 22px; }
  .contact svg { width: 12px; height: 12px; fill: var(--brand-blue); }
  .social {
    position: absolute;
    right: 48px; top: 196px;
    display: flex; gap: 8px;
  }
  .social span {
    width: 22px; height: 22px; border-radius: 50%;
    background: var(--brand-blue);
  }
  .rule { position: absolute; height: 1px; background: var(--rule); }
  .rule--contact { left: 290px; right: 40px; top: 226px; }
  .rule--services { left: 130px; width: 420px; top: 318px; }
  .services {
    position: absolute;
    left: 120px; width: 440px; top: 236px;
    text-align: center;
    font-size: 16px;
    line-height: 23px;
    color: var(--ink);
  }
</style>
</head>
<body>

  <section class="card card--back" aria-label="Card back">
    <div class="brand-lockup">
      <span class="brand-mark"></span>
      <span class="brand-name">Morvela Aesthetic Doctor</span>
    </div>
    <p class="back-tagline">Home &amp; Spa Based Treatments</p>
  </section>

  <section class="card card--front" aria-label="Card front">
    <div class="hero-art" role="img" aria-label="Soft blue flowing-hair profile emblem inside a thin grey ring"></div>

    <header class="identity">
      <h1 class="identity__name">DR. ELIN VARROW</h1>
      <p class="identity__credentials">MRCPCH MD<br>Australasian Diploma of Aesthetic Medicine</p>
    </header>

    <ul class="contact">
      <li>
        <svg viewBox="0 0 24 24" aria-hidden="true"><path d="M6.6 10.8a15 15 0 0 0 6.6 6.6l2.2-2.2a1 1 0 0 1 1-.25 11.4 11.4 0 0 0 3.6.57 1 1 0 0 1 1 1V20a1 1 0 0 1-1 1A17 17 0 0 1 3 4a1 1 0 0 1 1-1h3.5a1 1 0 0 1 1 1c0 1.25.2 2.45.57 3.57a1 1 0 0 1-.25 1z"/></svg>
        0800 555 014
      </li>
      <li>
        <svg viewBox="0 0 24 24" aria-hidden="true"><path d="M2 5h20v14H2z M2 5l10 8 10-8" /></svg>
        elin@morvela.co.nz
      </li>
      <li>
        <svg viewBox="0 0 24 24" aria-hidden="true"><circle cx="12" cy="12" r="10"/></svg>
        www.morvela.co.nz
      </li>
    </ul>

    <div class="social" aria-label="Social profiles"><span></span><span></span></div>
    <div class="rule rule--contact"></div>

    <p class="services">Dermal Injectables - Plasma Facials - Microneedling<br>Skin Boosters - Excessive Sweating<br>Home &amp; Spa Based Treatments</p>
    <div class="rule rule--services"></div>
  </section>

</body>
</html>
```